2022 Yearly Patron Circle (art gallery annual report)

6X9, 16-page brochure that serves both as an annual report for the previous year and gets mailed for an ask for donations. This must be done in InDesign and I will provide a template. I am also sending PDFs for the previous two years. Last year was pink and black, but I have recolored the logo purple this year.. so am open to whatever colors. I used last year's template to put in the new info. The theme for this year is Amazing - last year was Thriving. The font I chose for the front I do not want to use.. its just an example. All three pictures on the front don't have to be used.. just ideas.
Updates

I put three photos on the front page. It isn't necessary to use all of them, I thought there might be something there to use as part of the design

The current information is in the InDesign file, Calatalog Design.indd with the to Links Folders attached.

Target Market(s)

Donors

Industry/Entity Type

Art

Font styles to use
Sans Serif

Requirements
Must have
• InDesign
Nice to have
• A new look! Something different than 2021 an 2020 (PDFs included)

```html
<!DOCTYPE html>
<html lang="en">
<head>
<meta charset="utf-8">
<title>Collection – Yearly Patron Circle</title>
<link rel="stylesheet" href="https://fonts.googleapis.com/css2?family=Montserrat:wght@300;700&family=Oswald:wght@600&display=swap">
<style>
  :root {
    --purple: #8e4699;
    --ink: #231f20;
    --body: #4a4a4a;
    --paper: #ffffff;
    --art-warm: #c07a34;
    --art-dark: #5a3214;
    --photo-sky: #4f8fd6;
    --photo-wall: #b9bcc0;
  }
  html, body { margin: 0; padding: 0; overflow: hidden; }
  body { width: 1200px; height: 800px; background: var(--paper); position: relative; font-family: "Montserrat", sans-serif; }
  .page { position: absolute; inset: 0; overflow: hidden; }

  .brand-name {
    position: absolute; left: 43px; top: 92px;
    font-family: "Montserrat", sans-serif; font-weight: 700;
    font-size: 34px; letter-spacing: 3px; color: var(--ink);
    margin: 0; text-transform: uppercase; white-space: nowrap;
  }

  .section-tab { position: absolute; top: 71px; right: 0; height: 87px; display: flex; }
  .section-tab__rule { width: 8px; height: 100%; background: var(--purple); margin-right: 6px; }
  .section-tab__label {
    width: 391px; height: 100%; background: var(--purple); color: #fff;
    font-family: "Oswald", sans-serif; font-weight: 600; font-size: 57px;
    line-height: 87px; text-align: center; margin: 0; letter-spacing: -2px;
  }

  .side-rule { position: absolute; left: 103px; top: 213px; width: 4px; height: 392px; background: var(--purple); }

  .intro { position: absolute; left: 136px; top: 222px; width: 449px; color: var(--body); }
  .intro p {
    margin: 0 0 15px; font-weight: 300; font-size: 17.8px; line-height: 22.2px;
    text-align: justify; letter-spacing: 0.5px;
  }

  .artwork { position: absolute; top: 220px; width: 252px; height: 337px; }
  .artwork--painting { left: 619px; background: radial-gradient(circle at 45% 45%, #d9a25a 0%, var(--art-warm) 45%, var(--art-dark) 100%); }
  .artwork--sculpture { left: 895px; width: 254px; background: linear-gradient(90deg, var(--photo-wall) 0%, #d2d4d6 70%, var(--photo-sky) 100%); }

  .corner { position: absolute; background: var(--purple); }
  .corner--bl-v { left: 611px; top: 505px; width: 2px; height: 61px; }
  .corner--bl-h { left: 611px; top: 564px; width: 60px; height: 2px; }
  .corner--tr-h { left: 1099px; top: 211px; width: 59px; height: 2px; }
  .corner--tr-v { left: 1156px; top: 211px; width: 2px; height: 61px; }

  .folio { position: absolute; right: 0; top: 728px; display: flex; align-items: center; }
  .folio__theme {
    font-family: "Oswald", sans-serif; font-weight: 600; font-size: 42px;
    color: var(--purple); margin: 0; line-height: 44px; letter-spacing: -2px;
  }
  .folio__rule { width: 3px; height: 18px; background: var(--purple); margin: 0 4px 0 7px; }
  .folio__number {
    width: 60px; height: 18px; background: var(--purple); color: #fff;
    font-family: "Montserrat", sans-serif; font-weight: 700; font-size: 10px;
    line-height: 18px; padding-left: 9px; box-sizing: border-box;
  }
</style>
</head>
<body>
<main class="page">
  <h1 class="brand-name">Yearly Patron Circle</h1>

  <div class="section-tab">
    <div class="section-tab__rule"></div>
    <h2 class="section-tab__label">COLLECTION</h2>
  </div>

  <div class="side-rule"></div>

  <section class="intro">
    <p>Established in 1990, the Yearly Patron Circle permanent collection now consists of over 720 works of art valued at over $370,000.</p>
    <p>Sixty percent of the collection is currently on display in the Quillmere Valley College libraries, offices, conference rooms, and hallways on both the QVC main campus, Fernhollow campus, Ambervale and Larkspurn Learning Centers. Sharing our collection with staff, faculty, and students creates an aesthetic environment conducive to thought and inspiration.</p>
    <p>The collection increases each year with patron donations and through purchase awards.</p>
  </section>

  <div class="artwork artwork--painting" role="img" aria-label="Calligraphy painting in warm amber and brown tones with circular motif"></div>
  <div class="artwork artwork--sculpture" role="img" aria-label="Outdoor metal sculpture on a black pedestal beside a grey building"></div>

  <div class="corner corner--bl-v"></div>
  <div class="corner corner--bl-h"></div>
  <div class="corner corner--tr-h"></div>
  <div class="corner corner--tr-v"></div>

  <footer class="folio">
    <p class="folio__theme">AMAZING</p>
    <div class="folio__rule"></div>
    <div class="folio__number">11</div>
  </footer>
</main>
</body>
</html>
```